Create Social Media design templates for Online-Education-Startup

We are an online platform for pupils who provide group courses and on demand individual tutroing lessons. Our core values are personalisation, family and success. We need a holistic social media design concept which includes nine possible layouts for Instagram posts which reflect our values and promote not only our offerings and special deals but also support in building our brand image (for example: telling company history, daily news, funny facts, getting to know the team etc.).
Additionally, we need design elements for our YouTube channel:
-Videocover
-Cover Image for the channel

Our main colour is orange (RGB-Code: 255;105;31) and additional colours white, black, and grey. For the reference have a look at our website: www.lernquorvo.de.

Target Market(s)

We want to attract customers to our online tutoring courses and build a brand.

Industry/Entity Type

Education / Tutoring

Font styles to use
Sans Serif

Requirements
Must have
• Familiarize yourself with the style of our website. The designs should fit as well as possible.

```html
<!DOCTYPE html>
<html lang="en">
<head>
<meta charset="utf-8">
<title>Lernquorvo – Online Tutoring Post</title>
<link href="https://fonts.googleapis.com/css2?family=Poppins:wght@300;400;500;600;700&display=swap" rel="stylesheet">
<style>
  :root {
    --orange: rgb(255,105,31);
    --black: #0b0b0b;
    --white: #ffffff;
    --grey-bg: #e9e9ea;
    --card: #f6f7f9;
    --text-grey: #6b6b6b;
    --ink: #1a1a1a;
  }
  * { margin: 0; padding: 0; box-sizing: border-box; }
  html, body { width: 1200px; height: 796px; overflow: hidden; }
  body { background: var(--grey-bg); font-family: 'Poppins', sans-serif; color: var(--ink); position: relative; }

  .post { position: absolute; left: 220px; top: 18px; width: 760px; height: 760px; background: var(--white); overflow: hidden; box-shadow: 0 6px 24px rgba(0,0,0,.12); }

  .brand { position: absolute; left: 28px; top: 28px; display: flex; align-items: center; gap: 14px; }
  .brand-dot { width: 96px; height: 96px; border-radius: 50%; border: 7px solid var(--orange); }
  .brand-name { font-size: 30px; font-weight: 600; line-height: 1.15; color: var(--black); }
  .brand-sub { font-size: 26px; font-weight: 400; line-height: 1.2; color: var(--black); }
  .site-url { position: absolute; right: 48px; top: 42px; font-size: 16px; color: var(--orange); }

  .hero { position: absolute; left: 0; top: 137px; width: 760px; height: 179px; background: var(--orange); }
  .hero-title { position: absolute; left: 28px; top: 20px; color: var(--white); font-size: 37px; line-height: 44px; font-weight: 400; }
  .hero-title strong { font-weight: 700; }
  .hero-underline { position: absolute; left: 28px; top: 151px; width: 188px; height: 2px; background: var(--white); }

  .device { position: absolute; left: 454px; top: 185px; width: 276px; height: 163px; border-radius: 6px; background: linear-gradient(135deg, #3a3a3a 0%, #c9c2b8 45%, #ff8a4c 100%); }

  .section-title { position: absolute; left: 40px; top: 333px; font-size: 34px; font-weight: 400; color: var(--orange); }

  .card { position: absolute; top: 389px; width: 229px; height: 244px; background: var(--card); border-radius: 14px; box-shadow: 0 0 10px rgba(0,0,0,.06); padding: 18px 14px; }
  .card h3 { font-size: 19px; font-weight: 400; color: var(--ink); margin-bottom: 10px; }
  .card p { font-size: 11.6px; line-height: 18px; font-weight: 300; color: var(--text-grey); }
  .card ul { margin-top: 8px; padding-left: 10px; font-size: 11px; line-height: 15.5px; font-weight: 300; color: var(--text-grey); }
  .card-group { left: 27px; }
  .card-private { left: 266px; }
  .card-special { left: 505px; }

  .price { position: absolute; top: 547px; width: 128px; height: 128px; border-radius: 50%; background: var(--white); box-shadow: 0 2px 14px rgba(0,0,0,.1); text-align: center; padding-top: 26px; }
  .price-from { font-size: 10.5px; color: var(--ink); }
  .price-amount { font-size: 37px; font-weight: 600; color: var(--orange); line-height: 40px; }
  .price-note { font-size: 9.5px; line-height: 13px; color: var(--ink); }
  .price-group { left: 77px; }
  .price-private { left: 316px; }

  .footer-shapes { position: absolute; left: 0; top: 664px; }
  .trial { position: absolute; left: 27px; top: 708px; color: var(--black); font-size: 21px; font-weight: 600; }
  .trial span { font-size: 15px; font-weight: 400; color: var(--white); }
  .contact { position: absolute; right: 67px; top: 684px; text-align: right; }
  .contact-phone { font-size: 28px; color: var(--white); font-weight: 500; display: flex; align-items: center; gap: 10px; line-height: 34px; }
  .contact-mail { font-size: 13.5px; color: var(--orange); }
</style>
</head>
<body>
  <main class="post">
    <header>
      <div class="brand">
        <span class="brand-dot"></span>
        <div>
          <div class="brand-name">Lernquorvo</div>
          <div class="brand-sub">Bildungsinstitut</div>
        </div>
      </div>
      <div class="site-url">www.lernquorvo.de</div>
    </header>

    <section class="hero">
      <h1 class="hero-title"><strong>Online Tutoring</strong> with<br>Individual and Group<br>Lessons</h1>
      <div class="hero-underline"></div>
    </section>
    <div class="device" role="img" aria-label="Laptop showing the tutoring website with a smiling tutor"></div>

    <h2 class="section-title">Our courses</h2>

    <article class="card card-group">
      <h3>Group Courses</h3>
      <p>Our group courses are only conducted by very experienced trainers. The participation of several participants creates a great learning atmosphere.</p>
    </article>
    <article class="card card-private">
      <h3>Private Lessons</h3>
      <p>One-to-one instruction for individual support. Our trainer can therefore respond specifically to your individual needs.</p>
    </article>
    <article class="card card-special">
      <h3>Special Courses</h3>
      <p>At Lernquorvo we specialize in the special features of the school calender. Therefore, we offer a wide range of special courses.</p>
      <ul>
        <li>Holiday courses</li>
        <li>Power weekend courses</li>
        <li>Abitur preparation courses</li>
        <li>Preparation for the colloquium</li>
        <li>Final examination course secondary school</li>
      </ul>
    </article>

    <div class="price price-group">
      <div class="price-from">away</div>
      <div class="price-amount">12 €</div>
      <div class="price-note">per lesson<br>(45 minutes)</div>
    </div>
    <div class="price price-private">
      <div class="price-from">away</div>
      <div class="price-amount">24 €</div>
      <div class="price-note">per lesson<br>(45 minutes)</div>
    </div>

    <svg class="footer-shapes" width="760" height="96" viewBox="0 0 760 96">
      <rect x="0" y="12" width="760" height="84" fill="#f3f4f6"/>
      <path d="M330 34 C 390 34, 420 0, 470 0 L760 0 L760 96 L330 96 Z" fill="var(--black)"/>
      <path d="M0 20 L300 20 C 340 20, 360 40, 380 60 L418 96 L0 96 Z" fill="var(--orange)"/>
    </svg>
    <div class="trial">Free Trial Lesson <span>Available!</span></div>
    <div class="contact">
      <div class="contact-phone">
        <svg width="22" height="22" viewBox="0 0 24 24" aria-hidden="true"><path d="M6.6 10.8c1.4 2.8 3.8 5.1 6.6 6.6l2.2-2.2c.3-.3.7-.4 1-.2 1.1.4 2.3.6 3.6.6.6 0 1 .4 1 1V20c0 .6-.4 1-1 1C10.6 21 3 13.4 3 4c0-.6.4-1 1-1h3.5c.6 0 1 .4 1 1 0 1.3.2 2.5.6 3.6.1.3 0 .7-.2 1l-2.3 2.2z" fill="var(--white)"/></svg>
        089 4417 2093
      </div>
      <div class="contact-mail">kontakt@lernquorvo.de</div>
    </div>
  </main>
</body>
</html>
```